Metallic gold accent business card design using new logo

We need a new business card design utilizing our new logo and emphasizing a clean, sophisticated, elegant, easy to read card. Would like to use metallic gold accent, especially with the new logo design, but not overused. Thinking Black with metallic gold printing on reverse side. Front side off white in colour with logo or emblem, and basic information/writing. Logo and emblem should not be too large, would like the overall theme to be classic, even perhaps a bit understated.

Target Market(s)

High end custom home clientele. Sophisticated and elegant

Industry/Entity Type

Residential Construction

Contact Information for Business Card

Looking to use an online provider like ZIB or similar for printing the cards, if you need design details for applying the gold foil, it has to be set up as an element.

Font styles to use
Serif

Colors
fefbee

Requirements
Must have
• My information:
• Warren Pelt
• Owner
• war@hollowbeambuilders.ca
• (555) 317-4609 or (555) 726-4609
• www.hollowbeambuilders.ca
Should not have
• Colourful designs full of images or large logos, large text, flashy gold everywhere

```html
<!DOCTYPE html>
<html lang="en">
<head>
<meta charset="utf-8">
<title>Hollowbeam Builders — Business Card</title>
<link rel="stylesheet" href="https://fonts.googleapis.com/css2?family=Cormorant+Garamond:wght@500;600;700&display=swap">
<style>
  :root {
    --backdrop: #3b322d;
    --card-black: #141414;
    --card-offwhite: #fefbee;
    --gold: #b8903a;
    --gold-bright: #cfa84e;
    --ink-dark: #2a2622;
    --ink-muted: #6a625a;
    --divider: #c9bfa6;
  }
  * { margin: 0; padding: 0; box-sizing: border-box; }
  html, body { width: 1200px; height: 716px; overflow: hidden; }
  body {
    background: var(--backdrop);
    font-family: "Cormorant Garamond", Georgia, serif;
    position: relative;
  }
  .card {
    position: absolute;
    top: 215px;
    width: 500px;
    height: 286px;
    border-radius: 6px;
    box-shadow: 0 10px 30px rgba(0,0,0,.45);
  }
  .card--reverse {
    left: 70px;
    background: var(--card-black);
    border: 1px solid #222;
  }
  .card--front {
    left: 630px;
    background: var(--card-offwhite);
  }

  .brand {
    font-family: "Cormorant Garamond", Georgia, serif;
    font-weight: 700;
    letter-spacing: .22em;
    text-transform: uppercase;
    text-align: center;
    line-height: 1.3;
  }
  .card--reverse .brand {
    position: absolute;
    left: 0; right: 0;
    top: 50%;
    transform: translateY(-50%);
    font-size: 26px;
    color: var(--gold-bright);
  }
  .card--front .brand {
    position: absolute;
    top: 48px;
    right: 36px;
    width: 240px;
    font-size: 19px;
    color: var(--gold);
  }

  .holder {
    position: absolute;
    left: 36px;
    top: 112px;
  }
  .holder__name {
    color: var(--gold);
    font-weight: 700;
    font-size: 22px;
    line-height: 1.1;
  }
  .holder__title {
    color: var(--ink-muted);
    font-weight: 600;
    font-size: 14px;
    letter-spacing: .04em;
  }

  .divider {
    position: absolute;
    left: 230px;
    top: 150px;
    width: 1px;
    height: 104px;
    background: var(--divider);
  }

  .contact {
    position: absolute;
    left: 250px;
    top: 154px;
    list-style: none;
  }
  .contact__item {
    display: flex;
    align-items: center;
    gap: 9px;
    color: var(--ink-dark);
    font-weight: 600;
    font-size: 16px;
    line-height: 24px;
  }
  .contact__icon {
    width: 12px;
    height: 12px;
    flex: none;
  }
</style>
</head>
<body>
  <section class="card card--reverse" aria-label="Card reverse">
    <p class="brand">Hollowbeam<br>Builders</p>
  </section>

  <section class="card card--front" aria-label="Card front">
    <p class="brand">Hollowbeam Builders</p>

    <div class="holder">
      <p class="holder__name">Warren Pelt</p>
      <p class="holder__title">Owner</p>
    </div>

    <div class="divider"></div>

    <ul class="contact">
      <li class="contact__item">
        <svg class="contact__icon" viewBox="0 0 12 12"><rect width="12" height="12" rx="2" fill="#b8903a"/><rect x="4" y="2" width="4" height="8" rx="1" fill="#fefbee"/></svg>
        (555) 317-4609
      </li>
      <li class="contact__item">
        <svg class="contact__icon" viewBox="0 0 12 12"><rect width="12" height="12" rx="2" fill="#b8903a"/><rect x="4" y="2" width="4" height="8" rx="1" fill="#fefbee"/></svg>
        (555) 726-4609
      </li>
      <li class="contact__item">
        <svg class="contact__icon" viewBox="0 0 12 12"><rect width="12" height="12" rx="2" fill="#b8903a"/><rect x="2" y="3.5" width="8" height="5" fill="#fefbee"/><path d="M2 3.5 L6 6.5 L10 3.5" stroke="#b8903a" stroke-width="1" fill="none"/></svg>
        war@hollowbeambuilders.ca
      </li>
      <li class="contact__item">
        <svg class="contact__icon" viewBox="0 0 12 12"><rect width="12" height="12" rx="2" fill="#b8903a"/><circle cx="6" cy="6" r="3.6" stroke="#fefbee" stroke-width="1.2" fill="none"/><path d="M2.4 6 H9.6" stroke="#fefbee" stroke-width="1"/></svg>
        www.hollowbeambuilders.ca
      </li>
    </ul>
  </section>
</body>
</html>
```